Business Card Design

We are a home improvement and landscaping company based in South Eastern Connecticut hence the name BRIVALE. Landscaping & Home Renovation are our focus. Im looking for a very professional looking design. Something that will intergrade the two perfectly with bright but comfortable colors. The final design should communicate professionalism and trust worthiness in a place people feel most comfortable with their largest investment, that being their home.
Updates

Project Deadline Extended
Reason: I haven't come across a design that satisfies me.

Project Deadline Extended
Reason: Looking for more designs

Industry/Entity Type

Home Improvement

Contact Information for Business Card

Side one will contain my contact information
BRIVALE
Landscaping & Home Renovation
Gerald Matlock
5204139856
HIC.0381957
Side two will have a list of services:
Spring/Fall Clean-Ups
Property Management/Mowing
Lawn Care
Brush Clearing
Design Consultation
Interior Home Improvement
Kitchen, Bath & Office
Basement Finishing/Remodel
Flooring
Drywall
Paint
Doors & Windows
Trim & Base

```html
<!DOCTYPE html>
<html lang="en">
<head>
<meta charset="utf-8">
<title>BRIVALE Business Card</title>
<link href="https://fonts.googleapis.com/css2?family=Open+Sans:wght@300;400;600;700&display=swap" rel="stylesheet">
<style>
  :root {
    --bg: #8a6a45;
    --dark: #2b2d2e;
    --dark-2: #3a3d3f;
    --dark-3: #1f2122;
    --white: #ffffff;
    --paper: #f1f1f1;
    --grey-text: #6a6a6a;
    --green: #8fd14f;
    --orange: #e8622a;
    --orange-soft: #f08a5d;
    --list-text: #ececec;
  }
  * { margin: 0; padding: 0; box-sizing: border-box; }
  html, body {
    width: 1200px; height: 1023px; overflow: hidden;
    background: var(--bg);
    font-family: "Open Sans", Arial, sans-serif;
  }
  .canvas { position: relative; width: 1200px; height: 1023px; }
  .card {
    position: absolute; left: 230px; width: 740px; height: 423px;
    overflow: hidden; box-shadow: 0 12px 30px rgba(0,0,0,.35);
  }
  .card-front { top: 40px; background: linear-gradient(180deg, var(--white), var(--paper)); }
  .card-back {
    top: 540px;
    background: linear-gradient(160deg, var(--dark-2) 0%, var(--dark) 45%, var(--dark-3) 100%);
  }

  /* front */
  .front-header {
    position: absolute; left: 0; top: 0; width: 100%; height: 168px;
    background: linear-gradient(160deg, var(--dark-2), var(--dark-3));
    border-bottom: 10px solid var(--white);
    box-shadow: 0 4px 0 #bcbcbc;
  }
  .wordmark {
    position: absolute; left: 46px; top: 28px;
    font-weight: 300; font-size: 78px; line-height: 1; letter-spacing: 4px;
  }
  .front-header .wordmark { color: var(--green); }
  .tagline {
    position: absolute; left: 50px; top: 112px;
    font-weight: 300; font-size: 22px; padding-bottom: 4px;
    border-bottom: 2px solid var(--orange);
  }
  .front-header .tagline { color: var(--green); }
  .name-block { position: absolute; left: 50px; top: 240px; }
  .person-name { color: var(--orange); font-weight: 700; font-size: 34px; letter-spacing: 1px; text-transform: uppercase; }
  .person-role { color: var(--grey-text); font-size: 20px; margin-top: 2px; }
  .contact-list { position: absolute; right: 40px; top: 218px; list-style: none; }
  .contact-item { display: flex; align-items: center; gap: 10px; font-size: 20px; color: #222; margin-bottom: 8px; }
  .contact-icon { width: 20px; height: 20px; flex: none; }
  .footer-web {
    position: absolute; left: 0; bottom: 0; width: 420px; height: 56px;
    background: var(--dark); color: var(--white);
    font-size: 17px; letter-spacing: 7px; font-weight: 600;
    display: flex; align-items: center; padding-left: 46px;
  }
  .footer-licence {
    position: absolute; right: 0; bottom: 0; width: 340px; height: 56px;
    background: var(--orange); color: var(--dark-3); font-size: 20px;
    display: flex; align-items: center; justify-content: flex-end; padding-right: 40px;
  }
  .footer-chevron { position: absolute; left: 380px; bottom: 0; width: 60px; height: 56px; }

  /* back */
  .services { position: absolute; left: 60px; top: 34px; list-style: none; }
  .service { color: var(--list-text); font-size: 17px; line-height: 23px; display: flex; align-items: center; }
  .service::before {
    content: ""; width: 7px; height: 7px; border-radius: 50%;
    background: var(--orange); margin-right: 10px; flex: none;
  }
  .card-back .wordmark { color: var(--white); left: 60px; top: 288px; font-size: 64px; }
  .card-back .tagline { color: var(--white); left: 62px; top: 360px; font-size: 19px; border-bottom-color: var(--white); }
</style>
</head>
<body>
<main class="canvas">
  <section class="card card-front" aria-label="Business card front">
    <header class="front-header">
      <div class="wordmark">BRIVALE</div>
      <div class="tagline">Landscaping &amp; Home Renovation</div>
    </header>
    <div class="name-block">
      <div class="person-name">Gerald Matlock</div>
      <div class="person-role">Director</div>
    </div>
    <ul class="contact-list">
      <li class="contact-item">
        <svg class="contact-icon" viewBox="0 0 20 20"><circle cx="10" cy="10" r="10" fill="#e8622a"/><path d="M7 5h2l1 3-1.5 1a6 6 0 0 0 2.5 2.5L12 10l3 1v2c0 1-1 2-2 2A9 9 0 0 1 5 7c0-1 1-2 2-2z" fill="#fff"/></svg>
        520 413 9856
      </li>
      <li class="contact-item">
        <svg class="contact-icon" viewBox="0 0 20 20"><circle cx="10" cy="10" r="10" fill="#e8622a"/><rect x="5" y="6.5" width="10" height="7" fill="#fff"/><path d="M5 6.5l5 4 5-4" stroke="#e8622a" stroke-width="1.2" fill="none"/></svg>
        geraldmatlock@brivale.com
      </li>
    </ul>
    <div class="footer-web">www.brivale.com</div>
    <div class="footer-licence">HIC.0381957</div>
    <svg class="footer-chevron" viewBox="0 0 60 56" preserveAspectRatio="none">
      <polygon points="0,0 40,0 60,56 20,56" fill="#e8622a"/>
      <polygon points="0,0 30,0 10,56 0,56" fill="#2b2d2e"/>
      <line x1="30" y1="0" x2="10" y2="56" stroke="#fff" stroke-width="3"/>
    </svg>
  </section>

  <section class="card card-back" aria-label="Business card back">
    <ul class="services">
      <li class="service">Spring/Fall Clean-Ups</li>
      <li class="service">Property Management</li>
      <li class="service">Mowing</li>
      <li class="service">Lawn Care Brush Clearing</li>
      <li class="service">Design Consultation Interior</li>
      <li class="service">Home Improvement</li>
      <li class="service">Kitchen, Bath, Basement &amp; Office</li>
      <li class="service">Finishing/Remodel Flooring</li>
      <li class="service">Drywall/Paint</li>
      <li class="service">Doors &amp; Windows, Trim &amp; Base</li>
    </ul>
    <div class="wordmark">BRIVALE</div>
    <div class="tagline">Landscaping &amp; Home Renovation</div>
  </section>
</main>
</body>
</html>
```